Beilege-Broschüre Online Versand Kolvano.de
Zielgruppe
Bandagen, Orthesen und Sport-Schutzprodukte
Zielgruppe Menschen mit Verletzungen, Sportler und ältere Menschen.
Aufgabenstellung
Vorlage vorhanden und Format bereits festgelegt. Es geht um die kreative Umsetzung der gewünschten Inhalte und Vorbereitung zum druckfähigen Produkt.
Es handelt sich um einen Beileger für Versendungen im Online Bereich. Dieser soll unser Produktportfolio aufzeigen und mit vorhandenem Bildmaterial und Vorlagen erarbeitet werden.
eine INDD Vorlage steht zur Verfügung.

```html
<!DOCTYPE html>
<html lang="de">
<head>
<meta charset="utf-8">
<title>Kolvano.de – Knie</title>
<link rel="stylesheet" href="https://fonts.googleapis.com/css2?family=Open+Sans:wght@400;600;700;800&display=swap">
<style>
  :root {
    --teal: #17819c;
    --ink: #3a3a3a;
    --heading: #555555;
    --muted: #8a8a8a;
    --paper: #ffffff;
    --backdrop: #ecebe8;
    --photo-dark: #2b2f33;
    --photo-dark-top: #4a4f55;
    --photo-skin: #c49a7e;
    --photo-skin-top: #d9b49a;
    --photo-light: #e6e6e6;
    --photo-light-top: #f2f2f2;
    --photo-shade: #33383d;
  }
  * { box-sizing: border-box; margin: 0; padding: 0; }
  html, body { width: 1200px; height: 862px; overflow: hidden; }
  body {
    background: var(--backdrop);
    font-family: "Open Sans", Arial, sans-serif;
    color: var(--ink);
    position: relative;
  }
  .spread {
    position: absolute; left: 20px; top: 213px;
    width: 1160px; height: 436px;
    display: flex;
    box-shadow: 0 6px 24px rgba(0,0,0,.15);
  }
  .page { position: relative; width: 580px; height: 436px; background: var(--paper); overflow: hidden; }
  .band { position: absolute; background: var(--teal); height: 8px; }
  .photo { position: absolute; }
  .photo--dark { background: linear-gradient(160deg, var(--photo-dark-top), var(--photo-dark)); }
  .photo--skin { background: linear-gradient(160deg, var(--photo-skin-top), var(--photo-skin) 55%, var(--photo-shade)); }
  .photo--light { background: linear-gradient(160deg, var(--photo-light-top), var(--photo-light) 50%, var(--photo-shade)); }
  .num {
    position: absolute; height: 22px; width: 52px;
    background: var(--teal); color: #fff;
    font-weight: 700; font-size: 12px; font-style: italic;
    display: flex; align-items: center; justify-content: center;
  }
  .tab { position: absolute; background: var(--teal); width: 40px; height: 16px; }
  .heading {
    position: absolute; right: 25px; top: 40px;
    font-size: 22px; font-weight: 800; color: var(--heading); letter-spacing: .5px;
  }
  .heading-url {
    position: absolute; right: 25px; top: 72px;
    font-size: 6.5px; color: var(--teal);
  }
  .products { position: absolute; width: 240px; }
  .product { margin-bottom: 14px; }
  .product__title { font-size: 9.5px; font-weight: 600; color: var(--teal); line-height: 1.25; }
  .product__title b { font-weight: 700; }
  .product__text { font-size: 6.5px; color: var(--muted); line-height: 1.35; margin-top: 2px; }
  .product__sku { font-size: 9.5px; font-weight: 700; color: var(--teal); margin-top: 2px; }
  .product__price { font-size: 15px; font-weight: 800; color: var(--teal); margin-top: 2px; }
  .product__price small { font-size: 5.5px; font-weight: 400; color: var(--muted); margin-left: 4px; }
</style>
</head>
<body>
<main class="spread">
  <section class="page page--left">
    <div class="photo photo--skin" style="left:0;top:0;width:120px;height:215px" role="img" aria-label="Knieorthese mit Gelenkschienen am Bein"></div>
    <div class="photo photo--dark" style="left:120px;top:0;width:180px;height:215px" role="img" aria-label="Schwarze Kniebandage mit Patella-Polster"></div>
    <div class="photo photo--light" style="left:0;top:222px;width:140px;height:214px" role="img" aria-label="Schwarze Knieorthese mit Scharnieren"></div>
    <div class="photo photo--skin" style="left:145px;top:222px;width:165px;height:214px" role="img" aria-label="Offene Kniebandage mit Seitenstabilisatoren"></div>
    <div class="num" style="left:88px;top:190px">01</div>
    <div class="num" style="left:145px;top:190px">02</div>
    <div class="num" style="left:80px;top:236px">03</div>
    <div class="num" style="left:137px;top:236px">04</div>

    <div class="band" style="left:330px;top:0;width:250px"></div>
    <div class="band" style="left:300px;bottom:0;width:280px;height:6px"></div>

    <h1 class="heading">KNIE</h1>
    <p class="heading-url">https://www.kolvano.de/kniebandagen</p>

    <div class="products" style="left:325px;top:92px">
      <article class="product">
        <p class="product__title">01 - NR Support Z-FORTIS K47R<br><b>Kompressions Knöchelbandage</b></p>
        <p class="product__text">Die Z-Fortis Knöchelbandage ist eine hochwirksame Bandage zur Stabilisierung des Knöchelgelenkes nach Verletzungen und bei chronischen Instabilitäten.</p>
        <p class="product__sku">Artikelnummer: K47R</p>
        <p class="product__price">29,90 €<small>- inkl. 19 % MwSt. zzgl.</small></p>
      </article>
      <article class="product">
        <p class="product__title">02 - NR Support Z-FORTIS K47R<br><b>Kompressions Knöchelbandage</b></p>
        <p class="product__text">Die Z-Fortis Knöchelbandage ist eine hochwirksame Bandage zur Stabilisierung des Knöchelgelenkes nach Verletzungen und bei chronischen Instabilitäten.</p>
        <p class="product__sku">Artikelnummer: K47R</p>
        <p class="product__price">29,90 €<small>- inkl. 19 % MwSt. zzgl.</small></p>
      </article>
      <article class="product">
        <p class="product__title">03 - NR Support Z-FORTIS K47R<br><b>Kompressions Knöchelbandage</b></p>
        <p class="product__text">Die Z-Fortis Knöchelbandage ist eine hochwirksame Bandage zur Stabilisierung des Knöchelgelenkes nach Verletzungen und bei chronischen Instabilitäten.</p>
        <p class="product__sku">Artikelnummer: K47R</p>
        <p class="product__price">29,90 €<small>- inkl. 19 % MwSt. zzgl.</small></p>
      </article>
    </div>
  </section>

  <section class="page page--right">
    <div class="band" style="left:0;top:0;width:260px"></div>
    <div class="band" style="left:0;bottom:0;width:240px;height:6px"></div>

    <div class="products" style="left:22px;top:22px">
      <article class="product">
        <p class="product__title">04 - NR Support Z-FORTIS K47R<br><b>Kompressions Knöchelbandage</b></p>
        <p class="product__text">Die Z-Fortis Knöchelbandage ist eine hochwirksame Bandage zur Stabilisierung des Knöchelgelenkes nach Verletzungen und bei chronischen Instabilitäten.</p>
        <p class="product__sku">Artikelnummer: K47R</p>
        <p class="product__price">29,90 €<small>- inkl. 19 % MwSt. zzgl.</small></p>
      </article>
      <article class="product">
        <p class="product__title">05 - NR Support Z-FORTIS K47R<br><b>Kompressions Knöchelbandage</b></p>
        <p class="product__text">Die Z-Fortis Knöchelbandage ist eine hochwirksame Bandage zur Stabilisierung des Knöchelgelenkes nach Verletzungen und bei chronischen Instabilitäten.</p>
        <p class="product__sku">Artikelnummer: K47R</p>
        <p class="product__price">29,90 €<small>- inkl. 19 % MwSt. zzgl.</small></p>
      </article>
      <article class="product">
        <p class="product__title">06 - NR Support Z-FORTIS K47R<br><b>Kompressions Knöchelbandage</b></p>
        <p class="product__text">Die Z-Fortis Knöchelbandage ist eine hochwirksame Bandage zur Stabilisierung des Knöchelgelenkes nach Verletzungen und bei chronischen Instabilitäten.</p>
        <p class="product__sku">Artikelnummer: K47R</p>
        <p class="product__price">29,90 €<small>- inkl. 19 % MwSt. zzgl.</small></p>
      </article>
      <article class="product">
        <p class="product__title">07 - NR Support Z-FORTIS K47R<br><b>Kompressions Knöchelbandage</b></p>
        <p class="product__text">Die Z-Fortis Knöchelbandage ist eine hochwirksame Bandage zur Stabilisierung des Knöchelgelenkes nach Verletzungen und bei chronischen Instabilitäten.</p>
        <p class="product__sku">Artikelnummer: K47R</p>
        <p class="product__price">29,90 €<small>- inkl. 19 % MwSt. zzgl.</small></p>
      </article>
    </div>

    <div class="photo photo--dark" style="left:300px;top:0;width:135px;height:210px" role="img" aria-label="Knieorthese mit Gelenkschienen, Seitenansicht"></div>
    <div class="photo photo--skin" style="left:300px;top:216px;width:135px;height:220px" role="img" aria-label="Hautfarbene Kniebandage am Bein"></div>
    <div class="photo photo--light" style="left:441px;top:0;width:139px;height:235px" role="img" aria-label="Schwarze Kompressions-Kniebandage"></div>
    <div class="photo photo--light" style="left:441px;top:241px;width:139px;height:195px" role="img" aria-label="Gestrickte Kniebandage mit Patella-Ring"></div>
    <div class="tab" style="left:420px;top:150px"></div>
    <div class="tab" style="left:420px;top:205px"></div>
  </section>
</main>
</body>
</html>
```